Home Page PSD Website Design - 1 Page *

Design an eye-catching home page design for a rubbish removal website.

Please review the document provided it contains all the details and there is a second document with all the content for the page that needs to be included.

Target Market(s)

Home owners, businesses, property managers, real estate agents

Industry/Entity Type

Waste Management

Number of Pages Required

1 page

Requirements
Must have
• Please review the document provided it contains all the details and there is a second document with all the content for the page that needs to be included.

PSD must be layered, all elements labeled and separated for easy coding.
Nice to have

```html
<!DOCTYPE html>
<html lang="en">
<head>
<meta charset="utf-8">
<title>Brisk Junk Removal — Home</title>
<link href="https://fonts.googleapis.com/css2?family=Roboto:wght@400;500;700;900&display=swap" rel="stylesheet">
<style>
:root{
  --blue:#1f63b0;
  --blue-dark:#15437f;
  --navy:#17386f;
  --green:#93b51b;
  --green-dark:#6f8c0e;
  --ink:#222831;
  --text:#4a4f57;
  --muted:#8a9099;
  --pale:#f3f6fa;
  --white:#ffffff;
}
*{box-sizing:border-box;margin:0;padding:0}
html,body{width:1200px;height:4000px;overflow:hidden}
body{position:relative;background:var(--white);font-family:'Roboto',sans-serif;color:var(--ink)}
.abs{position:absolute}
.ph{position:absolute}
.btn{position:absolute;display:flex;align-items:center;justify-content:center;border-radius:30px;color:var(--white);font-weight:700;font-size:12px;letter-spacing:.3px}
.btn-green{background:linear-gradient(180deg,#a6c626,var(--green-dark))}
.btn-blue{background:linear-gradient(180deg,#2a76cc,var(--blue-dark))}

/* header */
.site-header{top:0;left:0;width:1200px;height:78px;background:var(--white)}
.brand{left:155px;top:22px;display:flex;align-items:center;gap:10px;font-size:21px;font-weight:900;color:var(--blue)}
.brand-mark{width:22px;height:22px;border-radius:50%;background:var(--green)}
.main-nav{left:457px;top:36px;display:flex;gap:20px;font-size:13px;font-weight:500;color:var(--ink)}
.header-phone{left:873px;top:25px;width:172px;height:38px;font-size:15px;font-weight:500;gap:8px}

/* hero */
.hero{top:78px;left:0;width:1200px;height:455px;background:linear-gradient(100deg,#1c4f93 0%,#2366b3 55%,#1d5aa3 100%)}
.hero-dots span{position:absolute;left:103px;width:8px;height:8px;border-radius:50%;border:1px solid rgba(255,255,255,.8)}
.hero-dots span.on{background:var(--white)}
.hero-title{left:155px;top:196px;font-size:48px;line-height:58px;font-weight:700;color:var(--white)}
.hero-text{left:156px;top:326px;width:430px;font-size:14px;line-height:24px;color:#dfe8f4}
.hero-art{left:668px;top:132px;width:520px;height:443px;border-radius:48% 42% 40% 46%;background:radial-gradient(circle at 40% 35%,#a7c53a 0%,#3f7fc4 45%,#1e4f97 80%)}

/* welcome */
.welcome-frame{left:255px;top:660px;width:312px;height:334px;border:2px solid var(--blue)}
.welcome-photo{left:158px;top:607px;width:379px;height:359px;background:linear-gradient(135deg,#8a8f96,#c07a3a 55%,#5e6268)}
.welcome-badge{left:613px;top:598px;width:40px;height:40px;border-radius:50%;background:linear-gradient(135deg,var(--green),var(--blue))}
.kicker{font-size:13px;color:var(--green-dark);font-weight:500}
.welcome-kicker{left:613px;top:654px}
.welcome-title{left:613px;top:682px;font-size:24px;font-weight:700}
.welcome-text{left:613px;top:726px;width:430px;font-size:12.5px;line-height:24px;color:var(--text)}
.call-icon{left:616px;top:875px}
.call-label{left:683px;top:870px;font-size:13px;color:var(--muted)}
.call-number{left:683px;top:888px;font-size:25px;font-weight:700;color:var(--blue)}

/* service */
.service{top:1022px;left:0;width:1200px;height:489px;background:var(--pale)}
.section-title{font-size:23px;font-weight:700;text-align:center;width:1200px;left:0}
.service-title{top:1078px}
.service-text{left:180px;top:1118px;width:840px;text-align:center;font-size:12.5px;line-height:24px;color:var(--text)}
.service-card{top:1219px;width:278px;height:211px;overflow:hidden}
.service-card .label{position:absolute;left:12px;bottom:12px;font-size:15px;font-weight:700;color:var(--white)}
.service-card .corner{position:absolute;right:0;bottom:0;width:0;height:0;border-left:40px solid transparent;border-bottom:34px solid var(--green)}
.service-card .corner i{position:absolute;right:6px;bottom:-27px;color:var(--white);font-style:normal;font-size:12px}

/* quote band */
.quote{top:1511px;left:0;width:1200px;height:416px;background:linear-gradient(90deg,#2a2f33 0%,#3b4148 45%,#6c7a6a 75%,#56604f 100%)}
.quote-title{left:163px;top:1602px;font-size:24px;font-weight:700;color:var(--white)}
.quote-text{left:163px;top:1654px;width:430px;font-size:12.5px;line-height:24px;color:#e6e8ea}

/* gallery */
.gallery-kicker{top:1966px;left:0;width:1200px;text-align:center}
.gallery-title{top:1994px}
.gallery-pair{top:2053px;height:261px;width:434px;display:flex;gap:3px}
.gallery-pair div{flex:1}
.before{background:linear-gradient(160deg,#9a8a70,#c9b89a 50%,#5f5a52)}
.after{background:linear-gradient(160deg,#b09a7c,#d6ccbd 60%,#8d8c89)}
.swap{position:absolute;top:2161px;width:46px;height:46px;border-radius:50%;background:var(--white);display:flex;align-items:center;justify-content:center;font-size:20px;color:var(--ink)}

/* why */
.why{top:2360px;left:0;width:1200px;height:466px;background:linear-gradient(180deg,#1d4e95,var(--navy))}
.why-art{left:47px;top:2405px;width:209px;height:372px;border-radius:40px;background:linear-gradient(180deg,#6a8fc3,#2e64ad 60%,#9eb93c)}
.why-title{left:540px;top:2410px;font-size:24px;font-weight:700;color:var(--white)}
.feature{position:absolute;display:flex;align-items:center;gap:14px;color:var(--white);font-size:14px;font-weight:500}
.feature svg{flex:none}

/* specialty */
.truck-art{left:0;top:2904px;width:489px;height:303px;border-radius:0 30px 40px 0;background:linear-gradient(90deg,#111 0%,#2a2a2a 48%,#e9ecef 52%,#f6f7f8 100%)}
.spec-title{left:536px;top:2899px;font-size:23px;font-weight:700}
.spec-text{left:534px;width:510px;font-size:12.5px;line-height:24px;color:var(--text)}

/* steps */
.steps-title{top:3354px;font-size:23px;font-weight:500}
.steps-title em{font-style:normal;color:var(--green)}
.step-label{position:absolute;font-size:14px;font-weight:700;text-align:center;width:200px}
.steps-art{left:1001px;top:3401px;width:140px;height:117px;border-radius:50%;background:linear-gradient(135deg,#a5c33a,#2c63ae)}

/* testimonials */
.testi-title{left:158px;top:3720px;font-size:24px;font-weight:700}
.testi-dots{left:1006px;top:3731px;display:flex;gap:7px}
.testi-dots span{width:6px;height:6px;border-radius:50%;background:#cfd3d8}
.testi-dots span.on{background:var(--green)}
.testi-card{position:absolute;top:3790px;width:281px;height:240px;background:var(--white);border:1px solid #e6e9ee;box-shadow:0 4px 14px rgba(0,0,0,.05)}
.testi-card .avatar{position:absolute;left:30px;top:28px;width:48px;height:48px;border-radius:50%;background:#c9ccd2}
.testi-card .name{position:absolute;left:97px;top:34px;font-size:14px;font-weight:500;color:var(--blue-dark)}
.testi-card .company{position:absolute;left:97px;top:56px;font-size:11px;color:var(--blue)}
.testi-card .quote-body{position:absolute;left:34px;top:98px;width:220px;font-size:12.5px;line-height:24px;color:var(--text)}
</style>
</head>
<body>

<header class="abs site-header">
  <div class="abs brand"><span class="brand-mark"></span>Brisk Junk Removal</div>
  <nav class="abs main-nav"><span>Available Services</span><span>Easy Online Quotes</span><span>Service Areas</span><span>FAQ</span></nav>
  <div class="btn btn-green header-phone">
    <svg width="14" height="14" viewBox="0 0 24 24"><path fill="#fff" d="M6.6 10.8a15 15 0 0 0 6.6 6.6l2.2-2.2c.3-.3.7-.4 1-.2 1.1.4 2.3.6 3.6.6.6 0 1 .4 1 1V20c0 .6-.4 1-1 1A17 17 0 0 1 3 4c0-.6.4-1 1-1h3.5c.6 0 1 .4 1 1 0 1.3.2 2.5.6 3.6.1.3 0 .7-.2 1z"/></svg>
    (555) 014-7720
  </div>
</header>

<section class="abs hero">
</section>
<div class="hero-dots"><span style="top:255px"></span><span class="on" style="top:280px"></span><span style="top:303px"></span></div>
<h1 class="abs hero-title">Full-Service Junk<br>Removal &amp; Hauling</h1>
<p class="abs hero-text">Lorem ipsum dolor sit amet, consectetur adipiscing elit, sed do eiusmod tempor incididunt ut labore et dolore.</p>
<div class="btn btn-green" style="left:155px;top:396px;width:163px;height:44px">REQUEST ESTIMATE</div>
<div class="ph hero-art" role="img" aria-label="Illustrated hero mascot carrying a large green trash can"></div>

<div class="abs welcome-frame"></div>
<div class="ph welcome-photo" role="img" aria-label="Photo of a smiling worker in a hard hat holding scrap metal"></div>
<div class="ph welcome-badge" role="img" aria-label="Small mascot illustration"></div>
<p class="abs kicker welcome-kicker">Got Junk To Haul? Give Us A Call!</p>
<h2 class="abs welcome-title">Welcome to Brisk Junk Removal</h2>
<p class="abs welcome-text">Has your Maplewood home, garage, basement, yard or place of business become cluttered with old appliances, furniture, electronics, yard debris, garbage or unwanted items that you have no use for? Call Brisk Junk Removal today and let us help make extra space in your home and around your property by removing all that stuff you no longer have use for.</p>
<svg class="abs call-icon" width="46" height="46" viewBox="0 0 46 46"><circle cx="23" cy="23" r="21" fill="none" stroke="#93b51b" stroke-width="2.5"/><path fill="#93b51b" d="M16 19.5a13 13 0 0 0 10.5 10.5l2.6-2.6c.3-.3.7-.4 1-.2l3 1c.4.1.6.5.6.9V32c0 .5-.4.9-.9.9A18 18 0 0 1 12.8 14c0-.5.4-.9.9-.9h3.1c.4 0 .8.2.9.6l1 3c.1.4 0 .7-.2 1z"/></svg>
<p class="abs call-label">Call Us 24*7:</p>
<p class="abs call-number">(555) 014-3390</p>

<section class="abs service"></section>
<h2 class="abs section-title service-title">Who Do We Service?</h2>
<p class="abs service-text">Whether you're a Maplewood homeowner, real estate agent, business owner, contractor, landlord, property manager or handling an estate, we've got you covered with our hassle-free &amp; speedy junk removal services. Sit back and relax while our crew does all the heavy lifting, carrying, loading and removal for you so you don't have to. Just show us what needs to be removed and our team will take care of rest.</p>
<div class="ph service-card" style="left:158px;background:linear-gradient(180deg,#b9c6d3,#6e6458 60%,#3f3a34)" role="img" aria-label="Photo of a two-storey brick house">
  <span class="label">Residential Services</span><span class="corner"><i>⟶</i></span></div>
<div class="ph service-card" style="left:461px;background:linear-gradient(180deg,#8fb3de,#4d6f97 60%,#55713e)" role="img" aria-label="Photo of a modern glass office building">
  <span class="label">Commercial Services</span><span class="corner"><i>⟶</i></span></div>
<div class="ph service-card" style="left:765px;background:linear-gradient(180deg,#b7c9de,#5d6670 55%,#3b4047)" role="img" aria-label="Photo of an apartment building with balconies">
  <span class="label">Property Managers and Realtors</span><span class="corner"><i>⟶</i></span></div>

<section class="ph quote" role="img" aria-label="Photo of movers carrying boxes from a truck"></section>
<h2 class="abs quote-title">Get Your Easy Online Quote Today!</h2>
<p class="abs quote-text">We make it really easy for you to receive your junk removal quote. With the power of the internet there is no need to disrupt your busy schedule with an in-person quote. To get started simply click the link below and you will be taken to our online quote form. You will receive your junk removal quote quickly and hassle free.</p>
<div class="btn btn-green" style="left:160px;top:1812px;width:178px;height:48px">REQUEST ESTIMATE</div>

<p class="abs kicker gallery-kicker">Our Works</p>
<h2 class="abs section-title gallery-title">Before &amp; After Gallery</h2>
<div class="ph gallery-pair" style="left:155px" role="img" aria-label="Before and after photos of a cleared garage"><div class="before"></div><div class="after"></div></div>
<div class="ph gallery-pair" style="left:612px" role="img" aria-label="Before and after photos of a cleared storage unit"><div class="before"></div><div class="after"></div></div>
<div class="swap" style="left:356px">↔</div>
<div class="swap" style="left:812px">↔</div>

<section class="abs why"></section>
<div class="ph why-art" role="img" aria-label="Illustrated mascot carrying a stack of household junk"></div>
<h2 class="abs why-title">Why Choose Us</h2>
<div class="feature" style="left:326px;top:2493px"><svg width="58" height="58" viewBox="0 0 58 58"><circle cx="29" cy="29" r="28" fill="#93b51b"/><circle cx="29" cy="29" r="13" fill="none" stroke="#fff" stroke-width="2.5"/><path d="M29 22v7l5 3" stroke="#fff" stroke-width="2.5" fill="none"/></svg>On Time, Every Time</div>
<div class="feature" style="left:562px;top:2493px"><svg width="58" height="58" viewBox="0 0 58 58"><circle cx="29" cy="29" r="28" fill="#93b51b"/><rect x="19" y="17" width="20" height="22" rx="3" fill="none" stroke="#fff" stroke-width="2.5"/><path d="M19 30h20M23 43v-4M35 43v-4" stroke="#fff" stroke-width="2.5"/></svg>Speedy Service</div>
<div class="feature" style="left:788px;top:2493px"><svg width="58" height="58" viewBox="0 0 58 58"><circle cx="29" cy="29" r="28" fill="#93b51b"/><path d="M29 40V24M29 30c-6 0-9-4-9-10 6 0 9 4 9 10zm0 0c6 0 9-4 9-10-6 0-9 4-9 10z" stroke="#fff" stroke-width="2.5" fill="none"/></svg>Protecting the Environment</div>
<div class="feature" style="left:326px;top:2596px"><svg width="58" height="58" viewBox="0 0 58 58"><circle cx="29" cy="29" r="28" fill="#93b51b"/><circle cx="29" cy="32" r="9" fill="none" stroke="#fff" stroke-width="2.5"/><path d="M25 18h8l-2 5h-4z" fill="#fff"/></svg>No Hidden Fees</div>
<div class="feature" style="left:562px;top:2596px"><svg width="58" height="58" viewBox="0 0 58 58"><circle cx="29" cy="29" r="28" fill="#93b51b"/><circle cx="29" cy="29" r="13" fill="none" stroke="#fff" stroke-width="2.5"/><path d="M23 29l4 4 8-8" stroke="#fff" stroke-width="2.5" fill="none"/></svg>Locally Owned</div>
<div class="feature" style="left:788px;top:2596px"><svg width="58" height="58" viewBox="0 0 58 58"><circle cx="29" cy="29" r="28" fill="#93b51b"/><rect x="15" y="21" width="18" height="13" fill="none" stroke="#fff" stroke-width="2.5"/><path d="M33 25h6l4 5v4H33z" fill="none" stroke="#fff" stroke-width="2.5"/><circle cx="21" cy="37" r="2.5" fill="#fff"/><circle cx="38" cy="37" r="2.5" fill="#fff"/></svg>Big or Small We Take it All!</div>
<div class="feature" style="left:326px;top:2701px"><svg width="58" height="58" viewBox="0 0 58 58"><circle cx="29" cy="29" r="28" fill="#93b51b"/><rect x="19" y="17" width="20" height="22" rx="3" fill="none" stroke="#fff" stroke-width="2.5"/><path d="M19 30h20M23 43v-4M35 43v-4" stroke="#fff" stroke-width="2.5"/></svg>Fully Insured</div>
<div class="feature" style="left:562px;top:2701px"><svg width="58" height="58" viewBox="0 0 58 58"><circle cx="29" cy="29" r="28" fill="#93b51b"/><path d="M29 40V24M29 30c-6 0-9-4-9-10 6 0 9 4 9 10zm0 0c6 0 9-4 9-10-6 0-9 4-9 10z" stroke="#fff" stroke-width="2.5" fill="none"/></svg>Cleaning Up</div>
<div class="feature" style="left:788px;top:2701px"><svg width="58" height="58" viewBox="0 0 58 58"><circle cx="29" cy="29" r="28" fill="#93b51b"/><circle cx="29" cy="32" r="9" fill="none" stroke="#fff" stroke-width="2.5"/><path d="M25 18h8l-2 5h-4z" fill="#fff"/></svg>Easy Online Quotes</div>

<div class="ph truck-art" role="img" aria-label="Illustration of a branded junk removal box truck"></div>
<h2 class="abs spec-title">Junk Removal is Our Specialty</h2>
<p class="abs spec-text" style="top:2940px">Over time, every business and household is sure to accumulate a number of unwanted items that end up collecting dust and taking up space. By contacting a junk hauling specialist to help you get rid of those items, you are saving yourself hours of hard work and possibly several trips to the dump. Brisk Junk Removal can do all that for you promptly and efficiently, making sure that you don't have to lift a finger or waste any precious time.</p>
<p class="abs spec-text" style="top:3088px">Take advantage of our professional junk removal service to clean out your Maplewood home, basement, garage or any other storage area of all types of unwanted items you want gone with ease. We can also clear away any rubbish and debris from your backyard and around your property.</p>
<div class="btn btn-green" style="left:537px;top:3204px;width:241px;height:53px">What CAN We Remove For You?</div>
<div class="btn btn-blue" style="left:790px;top:3204px;width:224px;height:53px">What CAN'T We Remove?</div>

<h2 class="abs section-title steps-title">Getting Rid of Unwanted Items, Junk &amp; Debris is As <em>Easy as 1, 2, 3 !</em></h2>
<svg class="abs" style="left:0;top:3440px" width="1200" height="160" viewBox="0 0 1200 160">
  <path d="M200 98 C240 80,260 78,278 78 M374 78 C420 80,440 90,565 102 M661 98 C720 78,780 70,855 76" fill="none" stroke="#b8bcc2" stroke-width="1.5" stroke-dasharray="4 4"/>
  <circle cx="200" cy="98" r="5" fill="#555"/>
  <path d="M458 86l5 3-5 3M770 71l5 3-5 3" fill="none" stroke="#555" stroke-width="1.5"/>
  <polygon points="326,30 374,54 374,102 326,126 278,102 278,54" fill="#93b51b"/>
  <polygon points="613,48 657,70 657,114 613,136 569,114 569,70" fill="#d9dbde"/>
  <polygon points="902,34 946,56 946,100 902,122 858,100 858,56" fill="#d9dbde"/>
  <text x="326" y="91" text-anchor="middle" font-family="Roboto,sans-serif" font-size="34" font-weight="700" fill="#222831">1</text>
  <text x="613" y="106" text-anchor="middle" font-family="Roboto,sans-serif" font-size="34" font-weight="700" fill="#222831">2</text>
  <text x="902" y="92" text-anchor="middle" font-family="Roboto,sans-serif" font-size="34" font-weight="700" fill="#222831">3</text>
</svg>
<p class="step-label" style="left:228px;top:3584px">Online Quote Form</p>
<p class="step-label" style="left:513px;top:3598px">Schedule a day</p>
<p class="step-label" style="left:799px;top:3581px">We Will Take Your Goods</p>
<div class="ph steps-art" role="img" aria-label="Illustrated mascot flying with a trash can"></div>

<h2 class="abs testi-title">Testimonials</h2>
<div class="abs testi-dots"><span class="on"></span><span></span><span></span></div>
<div class="testi-card" style="left:155px"><div class="avatar" role="img" aria-label="Customer portrait"></div><p class="name">Dana Whitlock</p><p class="company">Lorem Company</p><p class="quote-body">Integer vehicula, est vel posuere gravida, eros tellus fermentum magna, sit amet mattis mauris quam a nisl. Mauris vitae commodo elit.</p></div>
<div class="testi-card" style="left:461px"><div class="avatar" role="img" aria-label="Customer portrait"></div><p class="name">Dana Whitlock</p><p class="company">Lorem Company</p><p class="quote-body">Integer vehicula, est vel posuere gravida, eros tellus fermentum magna, sit amet mattis mauris quam a nisl. Mauris vitae commodo elit.</p></div>
<div class="testi-card" style="left:764px"><div class="avatar" role="img" aria-label="Customer portrait"></div><p class="name">Dana Whitlock</p><p class="company">Lorem Company</p><p class="quote-body">Integer vehicula, est vel posuere gravida, eros tellus fermentum magna, sit amet mattis mauris quam a nisl. Mauris vitae commodo elit.</p></div>

</body>
</html>
```